Help me make landing pages for my web application that are mobile friendly

I need to make 2 mobile friendly landing pages for an application. The 2 pages will be related. First I need a home page and then I need a working page. I do not want to change the color scheme or logos. Just layout and design.

```html
<!DOCTYPE html>
<html lang="en">
<head>
<meta charset="utf-8">
<title>ShiftDesk – Mobile Screens</title>
<link rel="stylesheet" href="https://fonts.googleapis.com/css2?family=Roboto:wght@400;500;700&display=swap">
<style>
:root{
  --bg:#323132;
  --teal:#2ea7d2;
  --purple:#6a4fa7;
  --grad:linear-gradient(90deg,#2ea7d2 0%,#6a4fa7 100%);
  --ink:#1f1f24;
  --muted:#555;
  --line:#e3e5ea;
  --ok:#4a9a3a;
  --bad:#e51f25;
  --white:#fff;
}
*{box-sizing:border-box;margin:0;padding:0}
html,body{width:1200px;height:2165px;overflow:hidden;background:var(--bg)}
body{font-family:"Roboto",Arial,sans-serif;color:var(--ink)}
.board{position:absolute;left:0;top:0;width:1063px;height:1918px;transform:scale(1.12888);transform-origin:0 0}
.screen{position:absolute;width:414px;background:var(--white);overflow:hidden}
.screen.home{left:86px;top:86px;height:1435px}
.screen.work{left:564px;top:86px;height:1747px}
.abs{position:absolute}
.hero{position:absolute;left:0;top:0}
.icon-btn{position:absolute;top:18px;width:40px;height:40px;border-radius:50%;background:#fff;display:flex;align-items:center;justify-content:center}
.brand{position:absolute;top:22px;left:96px;width:222px;text-align:center;color:#fff;font-size:25px;font-weight:500;line-height:30px}
.badge{position:absolute;left:139px;top:82px;width:136px;height:136px;border-radius:50%;background:#fff;box-shadow:0 6px 14px rgba(0,0,0,.12);display:flex;align-items:center;justify-content:center;color:var(--purple);font-size:20px;font-weight:500}
.tabs{position:absolute;left:0;top:244px;width:414px;height:33px;border-bottom:1px solid var(--line)}
.tab{position:absolute;top:2px;font-size:14px;font-weight:500;color:#222}
.tab.on{color:var(--teal);font-weight:700}
.tab-bar{position:absolute;bottom:-1px;height:3px;background:var(--teal)}
.pill-head{position:absolute;left:27px;top:301px;width:360px;height:46px;border-radius:23px;background:var(--grad);color:#fff;font-weight:700;font-size:15px;display:flex;align-items:center;padding:0 20px;gap:16px}
.pill-head .help{margin-left:auto}
.entry{position:absolute;left:26px;width:362px;height:196px;border-bottom:1px dashed #cfd2d8}
.entry .lbl{position:absolute;left:0;font-size:14px;font-weight:700;letter-spacing:.3px}
.entry .val{position:absolute;left:107px;font-size:15px;color:var(--muted)}
.entry .who{position:absolute;left:0;top:27px;font-size:15px;color:var(--muted);display:flex;align-items:center;gap:8px}
.entry .ok{color:var(--ok)}
.entry .bad{color:var(--bad)}
.photo{position:absolute;left:262px;width:96px;height:96px;border-radius:50%;border:3px solid #fff;box-shadow:0 4px 10px rgba(0,0,0,.18)}
.nav{position:absolute;left:0;width:414px;height:92px;border-top:1px solid var(--line)}
.nav-item{position:absolute;top:20px;transform:translateX(-50%);display:flex;flex-direction:column;align-items:center;gap:6px;font-size:14px;color:#111}
.nav-item.on{color:var(--purple)}
.field{position:absolute;left:26px;width:361px;height:46px;border-radius:23px;border:1px solid var(--line);box-shadow:0 2px 4px rgba(0,0,0,.04);display:flex;align-items:center;padding:0 22px;font-size:15px;color:#444}
.field b{color:var(--purple);font-weight:700;margin-right:16px}
.desc{position:absolute;left:26px;top:686px;width:361px;height:140px;border-radius:22px;border:1px solid var(--line);padding:16px 22px;font-size:14.5px;color:#444;line-height:26px}
.desc b{display:block;color:var(--purple);font-size:15px;margin-bottom:2px}
.comments{position:absolute;left:26px;top:847px;width:361px;height:178px;border-radius:20px;background:var(--grad);color:#fff;padding:14px 22px;font-size:15px}
.comments b{display:block;margin-bottom:8px}
.btn{position:absolute;height:36px;border-radius:18px;display:flex;align-items:center;justify-content:center;gap:10px;font-size:15px}
.btn.light{background:#fff;color:var(--teal);font-weight:700;font-size:13px}
.btn.teal{background:var(--teal);color:#fff}
.btn.purple{background:var(--purple);color:#fff}
.section{position:absolute;left:26px;font-size:14px;font-weight:700;color:var(--teal)}
.heading{position:absolute;left:27px;font-size:15.5px;font-weight:700;letter-spacing:.4px}
.meta{position:absolute;left:26px;font-size:15px;color:#555}
.meta b{color:#111;font-weight:700}
</style>
</head>
<body>
<svg width="0" height="0" style="position:absolute">
  <defs>
    <linearGradient id="hdr" x1="0" y1="0" x2="1" y2="0"><stop offset="0" stop-color="#2ea7d2"/><stop offset="1" stop-color="#6a4fa7"/></linearGradient>
    <symbol id="tick" viewBox="0 0 14 14"><circle cx="7" cy="7" r="7" fill="#4a9a3a"/><path d="M3.8 7.2l2.2 2.2 4.3-4.4" stroke="#fff" stroke-width="1.8" fill="none"/></symbol>
    <symbol id="grid" viewBox="0 0 20 20"><rect x="1" y="1" width="7.5" height="7.5" rx="1.5" fill="#2ea7d2"/><rect x="11.5" y="1" width="7.5" height="7.5" rx="3.7" fill="#6a4fa7"/><rect x="1" y="11.5" width="7.5" height="7.5" rx="1.5" fill="#6a4fa7"/><rect x="11.5" y="11.5" width="7.5" height="7.5" rx="1.5" fill="#2ea7d2"/></symbol>
    <symbol id="search" viewBox="0 0 20 20"><circle cx="9" cy="9" r="6" stroke="#2ea7d2" stroke-width="1.6" fill="none"/><path d="M13.5 13.5l4 4" stroke="#2ea7d2" stroke-width="1.6"/></symbol>
    <symbol id="user" viewBox="0 0 20 20"><circle cx="10" cy="6" r="4" fill="#2ea7d2"/><path d="M2.5 19c0-5 3.4-7.5 7.5-7.5s7.5 2.5 7.5 7.5z" fill="#2ea7d2"/></symbol>
    <symbol id="home" viewBox="0 0 24 24"><path d="M3 11l9-7 9 7M5 10v10h14V10M10 20v-5h4v5" stroke="currentColor" stroke-width="1.5" fill="none"/></symbol>
    <symbol id="opening" viewBox="0 0 24 24"><path d="M12 2v20M5 6h14v5H5zM3 14h18v5H3z" stroke="currentColor" stroke-width="1.5" fill="none"/></symbol>
    <symbol id="doc" viewBox="0 0 24 24"><path d="M7 3h9l4 4v14H7zM4 6v17h13M10 12h7M10 16h7" stroke="currentColor" stroke-width="1.5" fill="none"/></symbol>
    <symbol id="support" viewBox="0 0 24 24"><path d="M4 15v-3a8 8 0 0116 0v3M4 14h3v6H4zM17 14h3v6h-3zM20 20l-4 2h-3" stroke="currentColor" stroke-width="1.5" fill="none"/></symbol>
    <symbol id="logout" viewBox="0 0 24 24"><circle cx="12" cy="12" r="9" stroke="currentColor" stroke-width="1.5" fill="none"/><circle cx="12" cy="10" r="3" stroke="currentColor" stroke-width="1.5" fill="none"/><path d="M6.5 18.5c1.5-2.5 3.5-3.5 5.5-3.5s4 1 5.5 3.5" stroke="currentColor" stroke-width="1.5" fill="none"/></symbol>
    <symbol id="cal" viewBox="0 0 16 16"><rect x="1" y="3" width="14" height="12" rx="1.5" fill="#6a4fa7"/><path d="M4 1v4M12 1v4" stroke="#6a4fa7" stroke-width="2"/><path d="M3 7h10M3 10h10M3 13h10M6 7v7M10 7v7" stroke="#fff" stroke-width=".8"/></symbol>
  </defs>
</svg>

<main class="board">

  <!-- Home: My Assignments -->
  <section class="screen home">
    <svg class="hero" width="414" height="230"><path d="M0 0H414V97Q207 215 0 97Z" fill="url(#hdr)"/></svg>
    <div class="icon-btn" style="left:27px"><svg width="20" height="20"><use href="#grid"/></svg></div>
    <div class="brand">ShiftDesk</div>
    <div class="icon-btn" style="left:297px"><svg width="20" height="20"><use href="#search"/></svg></div>
    <div class="icon-btn" style="left:347px"><svg width="20" height="20"><use href="#user"/></svg></div>
    <div class="badge">ShiftDesk</div>

    <nav class="tabs">
      <span class="tab on" style="left:25px">MY ASSIGNMENTS</span>
      <span class="tab" style="left:201px">AVAILABLE OPENINGS</span>
      <span class="tab-bar" style="left:25px;width:127px"></span>
    </nav>

    <div class="pill-head">
      <svg width="14" height="14" viewBox="0 0 14 14"><path d="M3 1h9v10H3z M3 11l-1 2h9" fill="#fff"/></svg>
      MY ASSIGNMENTS
      <svg class="help" width="14" height="14" viewBox="0 0 14 14"><circle cx="7" cy="7" r="7" fill="#fff"/><text x="7" y="11" text-anchor="middle" font-size="10" font-weight="700" fill="#6a4fa7">?</text></svg>
    </div>

    <article class="entry" style="top:370px;height:169px">
      <span class="lbl" style="top:2px">SUBBING FOR:</span>
      <span class="who">Clara Whitfield, (Teacher) <svg width="14" height="14"><use href="#tick"/></svg></span>
      <span class="lbl" style="top:60px">LOCATION:</span><span class="val" style="top:59px">DVES</span>
      <span class="lbl" style="top:90px">STATUS:</span><span class="val ok" style="top:89px">Complete</span>
      <span class="lbl" style="top:120px">TIME SLOTS:</span><span class="val" style="top:119px">09/02 – 09/02 (1h 0m)</span>
      <div class="photo" style="top:-4px;background:linear-gradient(160deg,#8a6a4a,#2d5a4a)" role="img" aria-label="Portrait photo of the regular staff member"></div>
    </article>

    <article class="entry" style="top:566px;height:169px">
      <span class="lbl" style="top:2px">SUBBING FOR:</span>
      <span class="who">Extra duty (Teacher)</span>
      <span class="lbl" style="top:60px">LOCATION:</span><span class="val" style="top:59px">DVES</span>
      <span class="lbl" style="top:90px">STATUS:</span><span class="val ok" style="top:89px">Complete</span>
      <span class="lbl" style="top:120px">TIME SLOTS:</span><span class="val" style="top:119px">07/10 – 07/11 (1h 20m)</span>
    </article>

    <article class="entry" style="top:761px;height:169px">
      <span class="lbl" style="top:2px">SUBBING FOR:</span>
      <span class="who">Owen Harlow (Administrator) <svg width="14" height="14"><use href="#tick"/></svg></span>
      <span class="lbl" style="top:60px">LOCATION:</span><span class="val" style="top:59px">DVES</span>
      <span class="lbl" style="top:90px">STATUS:</span><span class="val ok" style="top:89px">Active</span>
      <span class="lbl" style="top:120px">TIME SLOTS:</span><span class="val" style="top:119px">07/26 – 08/07 (14h 15m)</span>
      <div class="photo" style="top:-1px;background:linear-gradient(160deg,#f2c9a8,#2a3344)" role="img" aria-label="Portrait photo of the regular staff member"></div>
    </article>

    <article class="entry" style="top:957px;height:169px">
      <span class="lbl" style="top:2px">SUBBING FOR:</span>
      <span class="who">Nadia Ellison (Teacher) <svg width="14" height="14"><use href="#tick"/></svg></span>
      <span class="lbl" style="top:60px">LOCATION:</span><span class="val" style="top:59px">DVES</span>
      <span class="lbl" style="top:90px">STATUS:</span><span class="val bad" style="top:89px">Canceled</span>
      <span class="lbl" style="top:120px">TIME SLOTS:</span><span class="val" style="top:119px">07/31 – 07/31 (9h 0m)</span>
      <div class="photo" style="top:-1px;background:linear-gradient(160deg,#f1f1f1,#c9b6a2)" role="img" aria-label="Portrait photo of the regular staff member"></div>
    </article>

    <article class="entry" style="top:1152px;height:169px;border-bottom:none">
      <span class="lbl" style="top:2px">SUBBING FOR:</span>
      <span class="who">Marcus Delaney (Teacher) <svg width="14" height="14"><use href="#tick"/></svg></span>
      <span class="lbl" style="top:60px">LOCATION:</span><span class="val" style="top:59px">DVES</span>
      <span class="lbl" style="top:90px">STATUS:</span><span class="val ok" style="top:89px">Active</span>
      <span class="lbl" style="top:120px">TIME SLOTS:</span><span class="val" style="top:119px">07/31 – 07/31 (9h 0m)</span>
      <div class="photo" style="top:-2px;background:linear-gradient(160deg,#eef2f6,#8fb2d6)" role="img" aria-label="Portrait photo of the regular staff member"></div>
    </article>

    <nav class="nav" style="top:1344px">
      <span class="nav-item" style="left:37px"><svg width="22" height="22"><use href="#home"/></svg>Home</span>
      <span class="nav-item" style="left:115px"><svg width="22" height="22"><use href="#opening"/></svg>Opening</span>
      <span class="nav-item on" style="left:205px"><svg width="22" height="22"><use href="#doc"/></svg>Assignment</span>
      <span class="nav-item" style="left:301px"><svg width="22" height="22"><use href="#support"/></svg>Support</span>
      <span class="nav-item" style="left:375px"><svg width="22" height="22"><use href="#logout"/></svg>Logout</span>
    </nav>
  </section>

  <!-- Working page: Opening Information -->
  <section class="screen work">
    <svg class="hero" width="414" height="230"><path d="M0 0H414V97Q207 215 0 97Z" fill="url(#hdr)"/></svg>
    <div class="icon-btn" style="left:27px"><svg width="20" height="20"><use href="#grid"/></svg></div>
    <div class="brand">ShiftDesk</div>
    <div class="icon-btn" style="left:297px"><svg width="20" height="20"><use href="#search"/></svg></div>
    <div class="icon-btn" style="left:347px"><svg width="20" height="20"><use href="#user"/></svg></div>
    <div class="badge">ShiftDesk</div>

    <nav class="tabs">
      <span class="tab on" style="left:25px">OPENING INFORMATION</span>
      <span class="tab-bar" style="left:25px;width:198px"></span>
    </nav>

    <div class="field" style="top:304px"><b>SUMMARY:</b>Testing-test</div>
    <div class="field" style="top:368px"><b>LOCATION:</b>Demo Valley Elementary School</div>
    <div class="field" style="top:431px"><b>TYPE:</b>Vacancy</div>
    <div class="field" style="top:495px"><b>REGULAR STAFF:</b>Simon Archer</div>
    <div class="field" style="top:559px"><b>ASSIGNMENT CATEGORY:</b>Teacher</div>
    <div class="field" style="top:622px"><b>DEPARTMENT:</b></div>
    <div class="desc"><b>DESCRIPTION:</b>Ut enim ad minima veniam, quis nostrum exer citationem ullam corporis suscipit labori osam, nisi ut aliquid ex ea commodi consequatur?</div>

    <div class="comments">
      <b>COMMENTS:</b>Write a comment or upload a file...
      <span class="btn light" style="left:22px;top:118px;width:93px">
        <svg width="14" height="12" viewBox="0 0 14 12"><path d="M1 1h5l5 5-5 5-5-5z" fill="#2ea7d2"/></svg>POST</span>
      <span class="btn light" style="left:127px;top:118px;width:114px">
        <svg width="12" height="12" viewBox="0 0 12 12"><path d="M6 1v7M3 4l3-3 3 3M1 9v2h10V9" stroke="#2ea7d2" stroke-width="1.8" fill="none"/></svg>UPLOAD</span>
    </div>

    <div class="field" style="top:1043px">
      <svg width="18" height="14" viewBox="0 0 18 14" style="margin-right:12px"><ellipse cx="7" cy="6" rx="6" ry="4.5" fill="#555"/><ellipse cx="12" cy="9" rx="5" ry="3.8" fill="#777"/></svg>No comments or files uploaded</div>

    <span class="section" style="top:1124px">ADDITIONAL DETAILS</span>
    <svg class="abs" style="left:0;top:1153px" width="414" height="4"><rect x="0" y="2.5" width="414" height="1" fill="#e3e5ea"/><rect x="26" y="0" width="157" height="3" fill="#2ea7d2"/></svg>
    <div class="field" style="top:1184px"><b>PARKING SPOT:</b></div>

    <span class="heading" style="top:1255px">TIME SLOTS</span>
    <span class="btn teal" style="left:27px;top:1291px;width:110px">
      <svg width="14" height="14" viewBox="0 0 14 14"><circle cx="7" cy="7" r="7" fill="#fff"/><path d="M3.8 7.2l2.2 2.2 4.3-4.4" stroke="#2ea7d2" stroke-width="1.8" fill="none"/></svg>Accept</span>
    <span class="btn purple" style="left:147px;top:1291px;width:120px">
      <svg width="14" height="14" viewBox="0 0 14 14"><circle cx="7" cy="7" r="7" fill="#fff"/><rect x="3.5" y="6" width="7" height="2" fill="#6a4fa7"/></svg>Withdraw</span>

    <div class="field" style="top:1352px"><svg width="16" height="16" style="margin-right:12px"><use href="#cal"/></svg><b>DATE:</b>03/09/2024</div>
    <div class="field" style="top:1417px;width:181px"><svg width="16" height="16" style="margin-right:12px"><use href="#cal"/></svg><b>FROM:</b>9.30 AM</div>
    <div class="field" style="top:1417px;left:223px;width:164px;padding:0 18px"><svg width="16" height="16" style="margin-right:12px"><use href="#cal"/></svg><b style="margin-right:8px">TO:</b>12.30 PM</div>

    <p class="meta" style="top:1491px"><b>CURRENT ASSIGNMENT:</b> No Assignment</p>
    <p class="meta" style="top:1519px"><b>STATUS:</b> Active</p>

    <span class="btn teal" style="left:174px;top:1565px;width:100px">
      <svg width="14" height="14" viewBox="0 0 14 14"><circle cx="7" cy="7" r="7" fill="#fff"/><path d="M3.8 7.2l2.2 2.2 4.3-4.4" stroke="#2ea7d2" stroke-width="1.8" fill="none"/></svg>Save</span>
    <span class="btn purple" style="left:287px;top:1565px;width:100px">
      <svg width="14" height="14" viewBox="0 0 14 14"><circle cx="7" cy="7" r="7" fill="#fff"/><rect x="3.5" y="6" width="7" height="2" fill="#6a4fa7"/></svg>Close</span>

    <nav class="nav" style="top:1649px">
      <span class="nav-item" style="left:37px"><svg width="22" height="22"><use href="#home"/></svg>Home</span>
      <span class="nav-item on" style="left:115px"><svg width="22" height="22"><use href="#opening"/></svg>Opening</span>
      <span class="nav-item" style="left:205px"><svg width="22" height="22"><use href="#doc"/></svg>Assignment</span>
      <span class="nav-item" style="left:301px"><svg width="22" height="22"><use href="#support"/></svg>Support</span>
      <span class="nav-item" style="left:375px"><svg width="22" height="22"><use href="#logout"/></svg>Logout</span>
    </nav>
  </section>

</main>
</body>
</html>
```